BRIGHT COLORFUL + 55 FAMILY HISTORY BROCHURE 11 x 17 bifold

11 x 17 Bifold Flyer I have given you the Layout I just need you to make it Pretty

YOU DO NOT NEED TO FOLLOW MY LAYOUT, You can but dont have too

Target Market(s)

55 year old consumers, who could choose our service of Hereditary Cancer Screening

Industry/Entity Type

Health And Wellness

Requirements
Must have
• Must be appealing to Grand Parents, must make them want to test , show lots of pictures of grand children, YOU DO NOT NEED TO FOLLOW MY LAYOUT , You can but dont have too
Nice to have
• use our colors of our logo , YOU DO NOT NEED TO FOLLOW MY LAYOUT , You can but dont have too
Should not have
• YOU DO NOT NEED TO FOLLOW MY LAYOUT, You can but dont have too

```html
<!DOCTYPE html>
<html lang="en">
<head>
<meta charset="utf-8">
<title>Hereditary Cancer Screening Brochure</title>
<link href="https://fonts.googleapis.com/css2?family=Playfair+Display:wght@700;900&family=Open+Sans:wght@400;600;700&display=swap" rel="stylesheet">
<style>
  :root{
    --navy:#1e2d6b;
    --navy-deep:#16224f;
    --green:#7ab83a;
    --green-light:#a3d35c;
    --stage:#5b5b5b;
    --paper:#ffffff;
    --text:#2b2b2b;
  }
  *{box-sizing:border-box;margin:0;padding:0}
  html,body{width:1200px;height:2400px;overflow:hidden}
  body{background:var(--stage);font-family:"Open Sans",Arial,sans-serif;color:var(--text);position:relative}
  .sheet{position:absolute;background:var(--paper);box-shadow:0 6px 18px rgba(0,0,0,.35);overflow:hidden}
  .sheet--cover{left:325px;top:50px;width:550px;height:712px}
  .sheet--outside{left:50px;top:830px;width:1100px;height:712px}
  .sheet--inside{left:50px;top:1620px;width:1100px;height:712px}
  .page{position:absolute;top:0;width:550px;height:712px;overflow:hidden}
  .page--left{left:0}
  .page--right{left:550px}
  .sheet--cover .page{left:0}
  .photo{position:absolute}

  /* cover */
  .cover-title{position:absolute;top:34px;left:0;width:100%;text-align:center;font-family:"Playfair Display",Georgia,serif;font-weight:700;color:var(--navy);font-size:31px}
  .cover-sub{position:absolute;top:76px;left:0;width:100%;text-align:center;font-family:"Playfair Display",Georgia,serif;font-weight:700;color:var(--green);font-size:25px}
  .cover-strip{position:absolute;top:126px;left:18px;right:18px;height:86px;display:flex;gap:6px}
  .cover-strip .photo{position:static;flex:1;border:2px solid #fff}
  .cover-question{position:absolute;top:224px;left:30px;right:30px;text-align:center;font-family:"Playfair Display",Georgia,serif;font-weight:700;color:var(--navy);font-size:21px;line-height:1.25}
  .cover-rule{position:absolute;top:286px;left:0;width:100%;height:4px;background:var(--navy-deep)}
  .cover-band{position:absolute;top:290px;left:0;width:100%;height:370px;background:linear-gradient(180deg,var(--navy) 0%,#2c4386 35%,#5b7fb0 60%,#6f9a4a 85%,var(--green) 100%)}
  .cover-band-text{position:absolute;top:22px;left:40px;right:40px;text-align:center;color:#fff;font-family:"Playfair Display",Georgia,serif;font-size:20px;line-height:1.35}
  .cover-hands{position:absolute;top:140px;left:0;width:100%;height:230px;background:radial-gradient(ellipse at 45% 45%,#d7a98a 0%,#b98468 22%,rgba(120,150,170,0) 55%)}
  .brand{position:absolute;font-family:"Open Sans",Arial,sans-serif;font-weight:700;font-size:14px;line-height:1;white-space:nowrap}
  .brand--light{color:#fff}
  .brand--navy{color:var(--navy)}
  .cover-brand{right:22px;bottom:18px}
  .footer-url{position:absolute;bottom:0;left:0;width:100%;height:52px;border-top:3px solid var(--green);display:flex;align-items:center;padding-left:28px;font-family:"Playfair Display",Georgia,serif;font-weight:700;color:var(--navy);font-size:16px;background:#fff}

  /* outside left */
  .hero{left:0;top:0;width:550px;height:300px;background:linear-gradient(135deg,#f2efe8 0%,#e9d3bf 35%,#c99a7b 55%,#a77b5b 75%,#e8e2d6 100%)}
  .ol-title{position:absolute;top:310px;left:0;width:100%;text-align:center;font-family:"Playfair Display",Georgia,serif;font-weight:900;color:var(--navy);font-size:27px}
  .ol-sub{position:absolute;top:348px;left:0;width:100%;text-align:center;font-family:"Playfair Display",Georgia,serif;font-weight:700;color:var(--navy);font-size:20px}
  .ol-callout{position:absolute;top:385px;left:22px;width:506px;height:110px;display:flex;border:2px solid var(--navy)}
  .ol-callout .photo{position:static;width:250px;height:100%;background:linear-gradient(120deg,#5a3b2a,#a7765a 50%,#3c2a22)}
  .ol-callout-text{flex:1;background:var(--navy);color:var(--green-light);font-family:"Playfair Display",Georgia,serif;font-size:12.5px;line-height:1.4;padding:14px}
  .ol-body{position:absolute;top:506px;left:26px;right:26px;color:var(--navy);font-weight:700;font-size:12.3px;line-height:1.42}
  .ol-body b{color:var(--green)}
  .ol-footer{position:absolute;bottom:0;left:0;width:100%;height:56px;border-top:3px solid var(--green);display:flex;align-items:center;justify-content:space-between;padding:0 26px;background:#fff}
  .ol-footer .url{font-family:"Playfair Display",Georgia,serif;font-weight:700;color:var(--navy);font-size:16px}
  .ol-footer .brand{position:static}

  /* inside */
  .inside-topbar{position:absolute;top:0;left:0;width:100%;height:12px;background:var(--green)}
  .il-photo{left:0;top:12px;width:550px;height:700px;background:linear-gradient(160deg,#dfe7d0 0%,#b7a58a 30%,#8b6b52 50%,#6f8f45 75%,#9cb867 100%)}
  .il-panel{position:absolute;top:22px;left:262px;width:276px;bottom:12px;background:rgba(255,255,255,.86);padding:12px;font-size:9.6px;line-height:1.38;color:#222}
  .il-panel p{margin-bottom:7px}
  .il-panel b{color:var(--navy)}
  .il-panel .lead{color:var(--green);font-weight:700}
  .il-quote{margin-top:6px;font-family:"Playfair Display",Georgia,serif;font-weight:700;color:var(--navy);font-size:15px;line-height:1.25}
  .ir-cols{position:absolute;top:22px;left:18px;right:18px;height:300px;display:flex;gap:14px;font-size:9.6px;line-height:1.38;color:#222}
  .ir-cols .col{flex:1}
  .ir-cols p{margin-bottom:7px}
  .ir-cols b{color:var(--navy)}
  .ir-photo{left:0;top:250px;width:550px;height:372px;background:linear-gradient(180deg,#e9eef2 0%,#cdb7a2 35%,#a98468 60%,#6d8e47 100%)}
  .ir-band{position:absolute;left:0;bottom:0;width:100%;height:90px;background:var(--navy);display:flex;align-items:center;justify-content:space-between;padding:0 22px}
  .ir-band-text{color:var(--green-light);font-family:"Playfair Display",Georgia,serif;font-weight:700;font-size:15px;line-height:1.3;max-width:330px}
  .ir-band .brand{position:static}
  .fold{position:absolute;left:549px;top:0;width:2px;height:100%;background:rgba(0,0,0,.06)}
</style>
</head>
<body>

<section class="sheet sheet--cover">
  <div class="page cover">
    <h1 class="cover-title">Hereditary Cancer Screening</h1>
    <p class="cover-sub">"The Test You Take For Them"</p>
    <div class="cover-strip">
      <div class="photo" role="img" aria-label="Grandmother hugging granddaughter" style="background:linear-gradient(135deg,#e6d4c2,#b88a6c)"></div>
      <div class="photo" role="img" aria-label="Grandparents with grandchild" style="background:linear-gradient(135deg,#d9c6b0,#9a7a5e)"></div>
      <div class="photo" role="img" aria-label="Smiling grandfather and grandson" style="background:linear-gradient(135deg,#cfd8c0,#a88266)"></div>
      <div class="photo" role="img" aria-label="Grandmother with grandchildren" style="background:linear-gradient(135deg,#e8dccc,#b99476)"></div>
      <div class="photo" role="img" aria-label="Three generations of a family" style="background:linear-gradient(135deg,#d6c9b6,#8f6f55)"></div>
    </div>
    <h2 class="cover-question">Will You give Your loved ones<br>the information to Beat Cancer in their lives ?</h2>
    <div class="cover-rule"></div>
    <div class="cover-band">
      <p class="cover-band-text">Give Them the Gift of Knowledge<br>knowing is better than not knowing.<br>Knowledge is Power</p>
      <div class="cover-hands" role="img" aria-label="Grandparent's hand holding a child's hand"></div>
      <div class="brand brand--light cover-brand">Kindred Wellness Co.</div>
    </div>
    <div class="footer-url">www.kinshipScreening.com</div>
  </div>
</section>

<section class="sheet sheet--outside">
  <div class="page page--left">
    <div class="photo hero" role="img" aria-label="Laughing grandfather being kissed by his granddaughter"></div>
    <h2 class="ol-title">DOES CANCER Run in Your Family?</h2>
    <p class="ol-sub">A Simple Swab Could SAVE a Family Members LIFE</p>
    <div class="ol-callout">
      <div class="photo" role="img" aria-label="Grandmother smiling with two grandchildren"></div>
      <p class="ol-callout-text">Your decision won't just affect you.<br>It will also impact Your Family,<br>share your test results may Forecast<br>Their Cancer Risks, too.</p>
    </div>
    <p class="ol-body">We believe it is important to understand what can and cannot be learned with genetic testing. <b>Genetic mutations can increase risks for certain cancers, but this does not mean cancer will definitely develop. You should be prepared to receive positive or negative results.</b> Most people receive Negative Results meaning no mutations associated with an increased risk for the Hereditary cancers.</p>
    <div class="ol-footer">
      <span class="url">www.kinshipScreening.com</span>
      <div class="brand brand--navy">Kindred Wellness Co.</div>
    </div>
  </div>
  <div class="fold"></div>
  <div class="page page--right">
    <h1 class="cover-title">Hereditary Cancer Screening</h1>
    <p class="cover-sub">"The Test You Take For Them"</p>
    <div class="cover-strip">
      <div class="photo" role="img" aria-label="Grandmother hugging granddaughter" style="background:linear-gradient(135deg,#e6d4c2,#b88a6c)"></div>
      <div class="photo" role="img" aria-label="Grandparents with grandchild" style="background:linear-gradient(135deg,#d9c6b0,#9a7a5e)"></div>
      <div class="photo" role="img" aria-label="Smiling grandfather and grandson" style="background:linear-gradient(135deg,#cfd8c0,#a88266)"></div>
      <div class="photo" role="img" aria-label="Grandmother with grandchildren" style="background:linear-gradient(135deg,#e8dccc,#b99476)"></div>
      <div class="photo" role="img" aria-label="Three generations of a family" style="background:linear-gradient(135deg,#d6c9b6,#8f6f55)"></div>
    </div>
    <h2 class="cover-question">Will You give Your loved ones<br>the information to Beat Cancer in their lives ?</h2>
    <div class="cover-rule"></div>
    <div class="cover-band">
      <p class="cover-band-text">Give Them the Gift of Knowledge<br>knowing is better than not knowing.<br>Knowledge is Power</p>
      <div class="cover-hands" role="img" aria-label="Grandparent's hand holding a child's hand"></div>
      <div class="brand brand--light cover-brand">Kindred Wellness Co.</div>
    </div>
    <div class="footer-url">www.kinshipScreening.com</div>
  </div>
</section>

<section class="sheet sheet--inside">
  <div class="inside-topbar"></div>
  <div class="page page--left">
    <div class="photo il-photo" role="img" aria-label="Grandfather and grandson outdoors in a garden"></div>
    <div class="il-panel">
      <p><span class="lead">Genetic testing revealed</span> Daniel Whitcomb carried a mutation that gave him a 70 to 80 percent chance of developing stomach cancer. Early screening revealed there were no signs of disease. Once the news sank in, he told us that testing saved his life.</p>
      <p><span class="lead">Genetic Testing Saved My Life.</span> Because of my age and family ancestry, my doctor recommended genetic testing, and they were right. I had the BRCA gene mutation. <b>Now I am prepared, and my sister will be tested too.</b></p>
      <p><span class="lead">A breast cancer survivor before me.</span> Marla Quinn was diagnosed with breast cancer two weeks before her 40th birthday. Knowing her result, I chose preventive care, and <b>my family now makes informed decisions.</b></p>
      <p><span class="lead">My father had genetic testing</span> and found he had hereditary colorectal cancer, known as Lynch syndrome. My name is Helen Ward and I am a proud survivor. <b>Following his example, I encourage every family to test.</b> Knowledge is power.</p>
      <p class="il-quote">A Positive result or finding a mutation is Not a Cancer Diagnosis and does not mean you will ever develop Cancer. Learning if you have an increased risk for cancer can make a difference</p>
    </div>
  </div>
  <div class="fold"></div>
  <div class="page page--right">
    <div class="ir-cols">
      <div class="col">
        <p><b>Genetic Testing</b> is done to determine whether family members without disease have inherited the same mutation as a family member who is known to carry a cancer associated mutation. Meaning: <b>Will You Help Save Kids &amp; Grand Children.</b></p>
        <p><b>What are the benefits of testing?</b> "The Power of Knowledge" <b>Helping Younger Family Members Know If there is a Risk and Preparing for it.</b> Knowing if you have a genetic mutation means you can work with your doctor to monitor and address your cancer risks. <b>According to the National Cancer Council eating 5 or more servings of Vegetables &amp; Fruits, and lowering your intake of red meat, dairy and eggs will help prevent or delay cancer.</b></p>
      </div>
      <div class="col">
        <p>There are many benefits to getting tested, regardless of the eventual result. If one of your family members — however distant — had cancer, there is a chance that you inherited a gene mutation that not only increases your personal risk of cancer, but also could be passed to the next generation. Those who are carriers of hereditary cancer gene mutations <b>could be at risk of getting cancer earlier in life than the general population. The sooner genetic testing is done, the more likely it is that the risk can be managed appropriately.</b></p>
      </div>
    </div>
    <div class="photo ir-photo" role="img" aria-label="Smiling three-generation family sitting together"></div>
    <div class="ir-band">
      <p class="ir-band-text">There are many known risk factors for Cancer. GENETICS and FAMILY HISTORY are Often Overlooked</p>
      <div class="brand brand--light">Kindred Wellness Co.</div>
    </div>
  </div>
</section>

</body>
</html>
```